We need a complete design for our construction company KELSO CONSTRUCTION based in Auckland New Zealand, we need a logo, website, business card, vehicle design etc..
We are a mid to high-end construction company who work mostly on residential projects and some commercial.

What we want to see in the design;
Professional,
Architectural,
Simple,
Alternative,

We want the design to communicate professionalism, high quality wormanship and and quality service.

Target Market(s)

People looking for a quality building/ construction company

Industry/Entity Type

Construction Company

Contact Information for Business Card

KELSO CONSTRUCTION.co.nz
Remi Tulvane
remi@kelsoconstruction-example.co.nz
021 5870 463

Logo Text

KELSO CONSTRUCTION

Number of Pages Required

5+ page

Font styles to use
Sans Serif

Colors

Designer to choose colors to be used in the design.

Requirements
Must have
• Must appear high end, professional, quality, be simple, easy to use, give security to potential clients
Nice to have
• high-quality photos of our recent projects
• about us page
• blog page
• contact us page
• high quality content
Should not have
• should not be hard to use and have too much going on.

```html
<!DOCTYPE html>
<html lang="en">
<head>
<meta charset="utf-8">
<title>Kelso Construction — Home</title>
<link href="https://fonts.googleapis.com/css2?family=Montserrat:wght@400;500;600;700&family=Raleway:wght@400;500;600&display=swap" rel="stylesheet">
<style>
  :root {
    --red: #b3141c;
    --ink: #111111;
    --grey: #8d8d8d;
    --text: #555555;
    --band: #e1e1e1;
    --card: #f3f3f3;
    --white: #ffffff;
  }
  * { box-sizing: border-box; margin: 0; padding: 0; }
  html, body { width: 1200px; height: 2655px; overflow: hidden; }
  body {
    position: relative;
    background: var(--white);
    font-family: "Raleway", sans-serif;
    color: var(--text);
  }
  .abs { position: absolute; }

  /* Header */
  .top-rule { left: 0; top: 0; width: 1200px; height: 5px; background: #222; }
  .brand { left: 78px; top: 18px; display: flex; align-items: center; gap: 12px; }
  .brand-mark { width: 44px; height: 44px; background: var(--red); }
  .brand-name { font-family: "Montserrat", sans-serif; font-weight: 600; color: var(--red); line-height: 1; }
  .brand-name .line1 { display: block; font-size: 46px; letter-spacing: 1px; }
  .brand-name .line2 { display: block; font-size: 15px; letter-spacing: 7.5px; margin-top: 6px; }
  .header-mail {
    right: 308px; top: 12px; font-size: 14px; color: #444;
    display: flex; align-items: center; gap: 10px; white-space: nowrap;
  }
  .header-phone {
    left: 906px; top: 4px; width: 214px; height: 32px; background: #222;
    clip-path: polygon(0 0, 100% 0, 95% 100%, 5% 100%);
    color: var(--white); font-family: "Montserrat", sans-serif; font-size: 20px;
    display: flex; align-items: center; justify-content: center; gap: 10px;
  }
  .nav { left: 0; top: 72px; width: 1200px; }
  .nav a {
    position: absolute; top: 0; font-family: "Raleway", sans-serif; font-size: 15px;
    color: #777; text-decoration: none; letter-spacing: 0.5px;
  }
  .nav a.active { color: var(--red); }
  .nav-underline { left: 552px; top: 116px; width: 84px; height: 4px; background: var(--red); }

  /* Hero */
  .hero {
    left: 0; top: 120px; width: 1200px; height: 574px;
    background:
      radial-gradient(ellipse 420px 260px at 900px 300px, rgba(236,240,248,0.85), rgba(236,240,248,0) 70%),
      linear-gradient(180deg, rgba(255,255,255,0) 75%, rgba(200,210,230,0.8) 100%),
      linear-gradient(90deg, #ecedf2 0%, #cfd6e8 40%, #a4b2d6 70%, #8d9fcb 100%);
  }
  .hero-title { left: 78px; top: 284px; font-family: "Montserrat", sans-serif; color: var(--ink); }
  .hero-title .small { display: block; font-size: 38px; font-weight: 400; letter-spacing: 3px; }
  .hero-title .big { display: block; font-size: 51px; font-weight: 700; letter-spacing: 2px; margin-top: 4px; }
  .hero-tag { left: 80px; top: 406px; font-family: "Montserrat", sans-serif; font-size: 20px; color: var(--ink); }
  .btn {
    position: absolute; display: flex; align-items: center; justify-content: center;
    font-family: "Montserrat", sans-serif; font-size: 20px; text-transform: uppercase;
  }
  .btn-solid { background: var(--ink); color: var(--white); }
  .btn-outline { border: 2px solid var(--ink); color: var(--ink); }
  .btn-red { border: 2px solid var(--red); color: var(--ink); }

  /* Value cards */
  .value-panel { left: 78px; top: 666px; width: 1044px; height: 205px; background: var(--white); }
  .value-card {
    position: absolute; top: 674px; width: 322px; height: 188px;
  }
  .value-card span {
    position: absolute; left: 22px; top: 68px; color: var(--white);
    font-family: "Montserrat", sans-serif; font-weight: 600; font-size: 25px; line-height: 1.1;
  }
  .slider-btn { top: 881px; width: 42px; height: 30px; border: 2px solid var(--ink); display: flex; align-items: center; justify-content: center; background: var(--white); }

  /* Section headings */
  .section-title {
    left: 0; width: 1200px; text-align: center;
    font-family: "Montserrat", sans-serif; font-weight: 700; font-size: 44px; letter-spacing: 0.5px;
  }
  .section-title .accent { color: var(--red); }
  .section-title .muted { color: var(--grey); }

  /* About */
  .about-copy { left: 149px; width: 902px; text-align: center; font-size: 14px; line-height: 23px; color: #555; }

  /* Projects */
  .projects-band { left: 0; top: 1312px; width: 1200px; height: 426px; background: var(--band); }
  .project-tile { position: absolute; top: 1458px; width: 244px; height: 158px; }

  /* News */
  .news-card { position: absolute; top: 1860px; width: 333px; height: 345px; background: var(--card); }
  .news-photo { position: absolute; left: 0; top: 0; width: 333px; height: 188px; }
  .news-badge { position: absolute; left: 138px; top: 160px; width: 56px; height: 56px; }
  .news-card h3 {
    position: absolute; left: 0; top: 230px; width: 333px; text-align: center;
    font-family: "Montserrat", sans-serif; font-weight: 600; font-size: 18px; color: var(--ink);
  }
  .news-card p {
    position: absolute; left: 28px; top: 262px; width: 277px; text-align: center;
    font-size: 13.5px; line-height: 19px; color: #777;
  }

  /* Contact */
  .contact-bg {
    left: 0; top: 2257px; width: 1200px; height: 333px;
    background:
      radial-gradient(ellipse 500px 260px at 820px 120px, rgba(220,224,230,0.7), rgba(220,224,230,0) 70%),
      linear-gradient(180deg, #f4f5f7 0%, #eceef1 60%, #f6f6f7 100%);
  }
  .footer-brand { left: 198px; top: 2383px; }
  .social { position: absolute; top: 2491px; width: 44px; height: 44px; border-radius: 50%; border: 2px solid var(--red); }
  .social.filled { background: var(--red); }
  .contact-line { position: absolute; left: 685px; display: flex; align-items: flex-start; gap: 12px; font-size: 15px; color: #555; line-height: 22px; }
  .contact-line.big { font-size: 19px; font-family: "Montserrat", sans-serif; }

  .footer-bar {
    left: 0; top: 2590px; width: 1200px; height: 65px; background: var(--red);
    color: var(--white); font-size: 13px; display: flex; align-items: center; justify-content: center;
  }
</style>
</head>
<body>

<header>
  <div class="abs top-rule"></div>
  <div class="abs brand">
    <div class="brand-mark"></div>
    <div class="brand-name"><span class="line1">KELSO</span><span class="line2">CONSTRUCTION</span></div>
  </div>
  <div class="abs header-mail">
    <svg width="18" height="14" viewBox="0 0 18 14"><rect x="0" y="0" width="18" height="14" rx="2" fill="#b3141c"/><path d="M1 2 L9 8 L17 2" stroke="#fff" stroke-width="1.6" fill="none"/></svg>
    info@kelsoconstruction-example.com
  </div>
  <div class="abs header-phone">
    <svg width="18" height="18" viewBox="0 0 24 24"><path d="M6.6 10.8a15.1 15.1 0 0 0 6.6 6.6l2.2-2.2a1 1 0 0 1 1-.25 11.4 11.4 0 0 0 3.6.57 1 1 0 0 1 1 1V20a1 1 0 0 1-1 1A17 17 0 0 1 3 4a1 1 0 0 1 1-1h3.5a1 1 0 0 1 1 1c0 1.25.2 2.45.57 3.57a1 1 0 0 1-.25 1z" fill="#fff"/></svg>
    123 456 7878
  </div>
  <nav class="abs nav">
    <a class="active" style="left:566px">HOME</a>
    <a style="left:667px">ABOUT US</a>
    <a style="left:795px">PROJECTS</a>
    <a style="left:915px">BLOGS</a>
    <a style="left:1014px">CONTACT US</a>
  </nav>
  <div class="abs nav-underline"></div>
</header>

<section>
  <div class="abs hero" role="img" aria-label="Modern two-storey white residential house with glass facade and pool, partly shown as architectural line drawing"></div>
  <h1 class="abs hero-title"><span class="small">KELSO</span><span class="big">CONSTRUCTION</span></h1>
  <p class="abs hero-tag">We Have New Fresh Ideas All The Time</p>
  <a class="btn btn-solid" style="left:78px; top:455px; width:168px; height:50px;">Read More</a>
  <a class="btn btn-outline" style="left:257px; top:455px; width:184px; height:50px;">Contact Us</a>
</section>

<section>
  <div class="abs value-panel"></div>
  <div class="value-card" style="left:85px; background:linear-gradient(120deg,#5b5d60 0%,#4a4b4e 50%,#6a4a3a 80%,#4a3a34 100%);" role="img" aria-label="Site engineers discussing plans"><span>Communicate<br>professionalism</span></div>
  <div class="value-card" style="left:439px; background:linear-gradient(120deg,#58595c 0%,#6b6256 50%,#4c5056 100%);" role="img" aria-label="Smiling builder in hard hat"><span>High quality<br>wormanship</span></div>
  <div class="value-card" style="left:793px; background:linear-gradient(120deg,#525456 0%,#5f5f5c 55%,#777877 100%);" role="img" aria-label="Engineer inspecting a construction site"><span style="top:80px">And quality service</span></div>
  <div class="abs slider-btn" style="left:554px">
    <svg width="18" height="10" viewBox="0 0 18 10"><path d="M0 5 L6 0 V3.5 H18 V6.5 H6 V10 Z" fill="#b3141c"/></svg>
  </div>
  <div class="abs slider-btn" style="left:603px">
    <svg width="18" height="10" viewBox="0 0 18 10"><path d="M18 5 L12 0 V3.5 H0 V6.5 H12 V10 Z" fill="#1a1a5a"/></svg>
  </div>
</section>

<section>
  <h2 class="abs section-title" style="top:982px"><span class="accent">ABOUT</span> <span class="muted">US</span></h2>
  <p class="abs about-copy" style="top:1054px">Lorem Ipsum is simply dummy text of the printing and typesetting industry. Lorem Ipsum has been the industry's standard dummy text ever since the 1500s, when an unknown printer took a galley of type and scrambled it to make a type specimen book. It has survived not only five centuries, but also the leap into electronic typesetting.</p>
  <p class="abs about-copy" style="top:1146px">Lorem Ipsum is simply dummy text of the printing and typesetting industry. Lorem Ipsum has been the industry's standard dummy text ever since the 1500s, when an unknown printer took...</p>
  <a class="btn btn-red" style="left:510px; top:1211px; width:180px; height:48px;">Read More</a>
</section>

<section>
  <div class="abs projects-band"></div>
  <h2 class="abs section-title" style="top:1358px"><span class="accent">FEATURED</span> <span class="muted">PROJECTS</span></h2>
  <div class="project-tile" style="left:78px; background:linear-gradient(160deg,#2a2d33,#6b7078 50%,#1d1f24);" role="img" aria-label="Arched steel and glass terminal interior"></div>
  <div class="project-tile" style="left:345px; background:linear-gradient(160deg,#2f6fb0,#c98a2c 55%,#6a5a2a);" role="img" aria-label="Workers in hard hats viewing a high-rise under construction"></div>
  <div class="project-tile" style="left:611px; background:linear-gradient(180deg,#1d3f8a 0%,#dfe3e8 45%,#39b7c9 80%,#7fd6df);" role="img" aria-label="Modern white villa with swimming pool"></div>
  <div class="project-tile" style="left:876px; background:linear-gradient(180deg,#4a76b8 0%,#8fa7c8 45%,#8a8176 100%);" role="img" aria-label="Engineers reviewing plans beside a steel frame structure"></div>
  <a class="btn btn-outline" style="left:526px; top:1637px; width:148px; height:48px;">View All</a>
</section>

<section>
  <h2 class="abs section-title" style="top:1786px"><span class="accent">LATEST</span> <span class="muted">NEWS</span></h2>

  <article class="news-card" style="left:78px">
    <div class="news-photo" style="background:linear-gradient(180deg,#3d4248,#a9b0b8 60%,#e7eaee);" role="img" aria-label="Looking up at glass skyscrapers"></div>
    <svg class="news-badge" viewBox="0 0 56 56"><polygon points="28,1 52,14.5 52,41.5 28,55 4,41.5 4,14.5" fill="#b3141c"/><rect x="19" y="20" width="18" height="16" rx="1.5" fill="none" stroke="#fff" stroke-width="2"/><line x1="19" y1="25" x2="37" y2="25" stroke="#fff" stroke-width="2"/><line x1="23" y1="17" x2="23" y2="22" stroke="#fff" stroke-width="2"/><line x1="33" y1="17" x2="33" y2="22" stroke="#fff" stroke-width="2"/></svg>
    <h3>Lorem ipsum is simply dummy text</h3>
    <p>Lorem Ipsum is simply dummy text of the printing and typesetting industry. Lorem Ipsum has been the industry's...</p>
  </article>

  <article class="news-card" style="left:434px">
    <div class="news-photo" style="background:linear-gradient(135deg,#8a7a66,#c9c0a8 45%,#3c5a88);" role="img" aria-label="Two builders in hard hats reviewing a tablet on site"></div>
    <svg class="news-badge" viewBox="0 0 56 56"><polygon points="28,1 52,14.5 52,41.5 28,55 4,41.5 4,14.5" fill="#b3141c"/><rect x="19" y="20" width="18" height="16" rx="1.5" fill="none" stroke="#fff" stroke-width="2"/><line x1="19" y1="25" x2="37" y2="25" stroke="#fff" stroke-width="2"/><line x1="23" y1="17" x2="23" y2="22" stroke="#fff" stroke-width="2"/><line x1="33" y1="17" x2="33" y2="22" stroke="#fff" stroke-width="2"/></svg>
    <h3>Lorem ipsum is simply dummy text</h3>
    <p>Lorem Ipsum is simply dummy text of the printing and typesetting industry. Lorem Ipsum has been the industry's...</p>
  </article>

  <article class="news-card" style="left:789px">
    <div class="news-photo" style="background:linear-gradient(135deg,#d9dadb,#8e9092 50%,#e6e7e8);" role="img" aria-label="Bright modern interior with glass walls"></div>
    <svg class="news-badge" viewBox="0 0 56 56"><polygon points="28,1 52,14.5 52,41.5 28,55 4,41.5 4,14.5" fill="#b3141c"/><rect x="19" y="20" width="18" height="16" rx="1.5" fill="none" stroke="#fff" stroke-width="2"/><line x1="19" y1="25" x2="37" y2="25" stroke="#fff" stroke-width="2"/><line x1="23" y1="17" x2="23" y2="22" stroke="#fff" stroke-width="2"/><line x1="33" y1="17" x2="33" y2="22" stroke="#fff" stroke-width="2"/></svg>
    <h3>Lorem ipsum is simply dummy text</h3>
    <p>Lorem Ipsum is simply dummy text of the printing and typesetting industry. Lorem Ipsum has been the industry's...</p>
  </article>
</section>

<footer>
  <div class="abs contact-bg" role="img" aria-label="Faint bright architectural interior backdrop"></div>
  <h2 class="abs section-title" style="top:2305px"><span class="accent">CONTACT</span> <span class="muted">US</span></h2>

  <div class="abs brand footer-brand">
    <div class="brand-mark"></div>
    <div class="brand-name"><span class="line1">KELSO</span><span class="line2">CONSTRUCTION</span></div>
  </div>
  <div class="social filled" style="left:196px"></div>
  <div class="social" style="left:251px"></div>
  <div class="social" style="left:305px"></div>
  <div class="social" style="left:360px"></div>
  <div class="social" style="left:417px"></div>

  <div class="contact-line" style="top:2380px">
    <svg width="20" height="26" viewBox="0 0 20 26"><path d="M10 1a8 8 0 0 0-8 8c0 6 8 15 8 15s8-9 8-15a8 8 0 0 0-8-8z" fill="none" stroke="#b3141c" stroke-width="1.8"/><circle cx="10" cy="9" r="3" fill="none" stroke="#b3141c" stroke-width="1.8"/></svg>
    <span>123, Lorem ipsum dummy text,<br>Country - 123456.</span>
  </div>
  <div class="contact-line big" style="top:2448px">
    <svg width="22" height="22" viewBox="0 0 24 24"><path d="M6.6 10.8a15.1 15.1 0 0 0 6.6 6.6l2.2-2.2a1 1 0 0 1 1-.25 11.4 11.4 0 0 0 3.6.57 1 1 0 0 1 1 1V20a1 1 0 0 1-1 1A17 17 0 0 1 3 4a1 1 0 0 1 1-1h3.5a1 1 0 0 1 1 1c0 1.25.2 2.45.57 3.57a1 1 0 0 1-.25 1z" fill="none" stroke="#b3141c" stroke-width="1.8"/></svg>
    <span>123 456 7878</span>
  </div>
  <div class="contact-line big" style="top:2497px">
    <svg width="22" height="18" viewBox="0 0 22 18" style="margin-top:3px"><rect x="1" y="1" width="20" height="16" fill="none" stroke="#b3141c" stroke-width="1.6"/><path d="M1 2 L11 10 L21 2" fill="none" stroke="#b3141c" stroke-width="1.6"/></svg>
    <span>info@kelsoconstruction-example.com</span>
  </div>

  <div class="abs footer-bar">© KELSO Constructions. &nbsp;- 2018 All Right Reserved</div>
</footer>

</body>
</html>
```